Bref créative |
Wordpress Website for Law Office | ||
Law Offices of Dorian Thackeray | ||
Law | ||
www.dthackerlegal.example | ||
Law Offices | ||
Clean/Simple Professional Content Driven Friendly Academic Sophisticated Elegant Service Oriented Traditional |
top | ||
www.dthackerlegal.example/logo.pdf | ||
I want my current website, dthackerlegal.example, redesigned using my logo, http://www.dthackerlegal.example/logo.pdf. The menus will be the same. The content will be the same. The layout should be similar. All I am looking for is a new design. Once the design is selected, the wordpress theme will be created based on it. |

```html
<!DOCTYPE html>
<html lang="en">
<head>
<meta charset="utf-8">
<title>Law Offices of Dorian Thackeray</title>
<link href="https://fonts.googleapis.com/css2?family=Cinzel:wght@400;700&family=Arimo:wght@400;700&display=swap" rel="stylesheet">
<style>
:root{
  --navy:#0d3f7a;
  --blue:#1c63b0;
  --blue-light:#3b86d1;
  --ink:#333;
  --muted:#666;
  --grey-bg:#e6e8ea;
  --panel:#ffffff;
  --box:#eef0f2;
  --box-edge:#c9ced4;
  --dark:#3d3f42;
}
*{margin:0;padding:0;box-sizing:border-box}
html,body{width:1200px;height:1023px;overflow:hidden}
body{background:linear-gradient(#f4f5f6,#dfe2e5);font-family:Arimo,Arial,sans-serif;color:var(--ink);position:relative}
.topbar{position:absolute;left:0;top:0;width:1200px;height:26px;background:linear-gradient(90deg,#0b3566,#1d62ad 60%,#0b3566)}
.tollfree{position:absolute;right:20px;top:0;height:30px;padding:0 18px;background:#fff;border-radius:0 0 0 14px;font:italic 700 17px/30px Arimo,Arial,sans-serif;color:#8a8f96;letter-spacing:.5px}
.tollfree b{color:var(--blue);font-size:27px;vertical-align:-2px}
.brand{position:absolute;left:135px;top:58px;display:flex;align-items:center;gap:18px}
.brand-mark{width:60px;height:60px;background:var(--blue)}
.brand-name{font:400 34px/1.1 Cinzel,serif;color:var(--navy);width:480px}
.statue{position:absolute;left:712px;top:34px;width:205px;height:126px;background:radial-gradient(ellipse at 55% 45%,#b7bdc3,#e8eaec 70%)}
.utility{position:absolute;left:932px;top:42px;list-style:none}
.utility li{display:flex;align-items:center;gap:8px;height:22px;margin-bottom:7px;width:158px;padding:0 6px;background:linear-gradient(#fff,#e7e9eb);border:1px solid #c7ccd2;border-radius:3px;font-size:11px;color:var(--navy)}
.utility i{width:12px;height:12px;background:var(--blue-light);border-radius:2px;flex:none}
.nav{position:absolute;left:133px;top:167px;width:937px;height:38px;background:linear-gradient(#2a74c2,#0e478a);border-radius:6px;display:flex;align-items:center;padding:0 12px}
.nav a{color:#fff;text-decoration:none;font:700 13px Arimo,Arial,sans-serif;padding:0 17px;line-height:38px}
.nav a.active{background:linear-gradient(#5a9be0,#2467b3);box-shadow:inset 0 0 0 1px #79b0ea}
.search{margin-left:auto;width:150px;height:22px;background:#fff;border-radius:3px;font-size:11px;color:#999;padding:0 8px;line-height:22px;position:relative}
.search svg{position:absolute;right:6px;top:5px}
.main{position:absolute;left:133px;top:216px;width:937px;height:402px;background:var(--panel);border:1px solid #d4d8dc;border-radius:4px}
.welcome{position:absolute;left:20px;top:20px;width:560px}
.welcome h1{font:400 23px Cinzel,serif;color:#222;display:flex;align-items:center;gap:10px;margin-bottom:20px}
.welcome h1 span{width:18px;height:18px;background:var(--blue);transform:rotate(45deg)}
.welcome p{font-size:12.5px;line-height:1.45;margin-bottom:14px}
.welcome a{color:var(--blue)}
.points{list-style:none;margin:6px 0 18px}
.points li{font-size:12.5px;line-height:1.4;padding-left:28px;position:relative;margin-bottom:8px}
.points li::before{content:"";position:absolute;left:4px;top:2px;width:12px;height:12px;background:var(--blue);transform:rotate(45deg)}
.practice{position:absolute;left:612px;top:12px;width:312px}
.practice h2{height:42px;background:linear-gradient(#55585c,#2f3134);border-radius:6px;color:#fff;font:400 21px/42px Cinzel,serif;padding-left:40px;position:relative}
.practice h2::before{content:"";position:absolute;left:14px;top:14px;width:13px;height:13px;background:#fff;transform:rotate(45deg)}
.practice .intro{font-size:12px;line-height:1.4;padding:8px 10px;background:#f4f5f6}
.areas{list-style:none;padding:0 10px}
.areas li{display:flex;align-items:center;gap:12px;height:40px;border-bottom:1px dotted #c6cbd0;font:700 13px Arimo,Arial,sans-serif;color:var(--blue)}
.areas i{width:24px;height:24px;border-radius:50%;background:linear-gradient(#6aa6e3,#1c5ea6)}
.practice .note{font-size:11.5px;line-height:1.38;padding:8px 10px 0}
.practice .note a{color:var(--blue)}
.offices{position:absolute;left:133px;top:628px;width:937px;height:270px;display:grid;grid-template-columns:repeat(3,265px);gap:14px 40px;justify-content:center;padding-top:10px}
.office{background:linear-gradient(#f6f7f8,#e3e6e9);border:1px solid var(--box-edge);border-radius:6px;text-align:center;height:116px}
.office h3{font:700 18px/38px Cinzel,serif;color:var(--navy);border-bottom:1px solid var(--box-edge);margin:0 10px}
.office p{font-size:11.5px;line-height:1.38;padding-top:8px;color:#444}
.footer{position:absolute;left:133px;top:900px;width:937px;height:123px;background:linear-gradient(#1d62ad,#0b3566);border-radius:6px 6px 0 0;color:#dfe9f6;text-align:center}
.footer .links{font:700 11.5px Arimo,Arial,sans-serif;color:#fff;padding-top:14px}
.footer .links a{color:#fff;text-decoration:none;margin:0 3px}
.footer .about{font-size:11px;line-height:1.45;width:800px;margin:10px auto 0}
.footer .legal{position:absolute;left:0;right:0;bottom:12px;font-size:11px}
.social{position:absolute;right:60px;bottom:11px;display:flex;gap:4px}
.social i{width:15px;height:15px;background:#dfe9f6;border-radius:2px}
</style>
</head>
<body>
<div class="topbar"></div>
<div class="tollfree">CALL TOLL FREE <b>(800) 555-0187</b></div>

<header>
  <div class="brand">
    <div class="brand-mark"></div>
    <div class="brand-name">Law Offices of Dorian Thackeray</div>
  </div>
  <div class="statue" role="img" aria-label="Illustration of a justice statue holding scales"></div>
  <ul class="utility">
    <li><i></i>Join Our Mailing List</li>
    <li><i></i>Add This To Favorites</li>
    <li><i></i>Log Into My File 24/7</li>
    <li><i></i>Languages Spoken</li>
  </ul>
</header>

<nav class="nav">
  <a href="#">Home Page</a>
  <a href="#" class="active">Practice Areas</a>
  <a href="#">Why Us</a>
  <a href="#">Our Fees</a>
  <a href="#">Free Advice</a>
  <a href="#">Contact Us</a>
  <a href="#">Closing Tips</a>
  <div class="search">Search
    <svg width="12" height="12" viewBox="0 0 12 12"><circle cx="5" cy="5" r="3.5" fill="none" stroke="#1c63b0" stroke-width="1.5"/><line x1="7.6" y1="7.6" x2="11" y2="11" stroke="#1c63b0" stroke-width="1.5"/></svg>
  </div>
</nav>

<main class="main">
  <section class="welcome">
    <h1><span></span>Welcome to our site</h1>
    <p>The Law Offices of Dorian Thackeray is dedicated to providing the highest quality legal advice and counseling to clients throughout New York State. We offer extensive knowledge and experience in <a href="#">Real Estate</a> and <a href="#">Business Law</a>.</p>
    <p>When faced with a legal question, choosing the right law firm is a critical first step in resolving the issue. By choosing the Law Offices of Dorian Thackeray, you are choosing a firm that:</p>
    <ul class="points">
      <li>Provides individualized service that gives its clients confidence and peace of mind.</li>
      <li>Possesses vast experience and resources that enables it to handle your legal needs in a professional manner with efficiency, clarity, and resolve.</li>
      <li>Charges reasonable and straight-forward prices for the legal services rendered.</li>
    </ul>
    <p>Individuals and business entities alike have placed their trust in the Law Offices of Dorian Thackeray for one simple reason: they know they will be represented by highly skilled and dedicated attorneys who provide a level of sophistication and a value proposition that is unmatched. Please take a moment to browse through our website to learn how we can help you.</p>
  </section>

  <aside class="practice">
    <h2>Practice Areas</h2>
    <p class="intro">We have extensive experience in the areas of law listed below.</p>
    <ul class="areas">
      <li><i></i>Business Law</li>
      <li><i></i>Internet Law</li>
      <li><i></i>Real Estate Law</li>
      <li><i></i>Wills &amp; Trusts Law</li>
    </ul>
    <p class="note">Please click on the link above for a detailed description of each practice area.</p>
    <p class="note">If you need representation in any area of law not listed above, please <a href="#">contact us</a>. We have many experienced attorneys that we work with and we will be happy to refer you to an attorney who can handle your matter.</p>
  </aside>
</main>

<section class="offices">
  <div class="office"><h3>Brooklyn Office</h3><p>1840 Harbor Lane, 2nd Floor<br>Brooklyn, NY 11299<br>(718) 555-0142</p></div>
  <div class="office"><h3>Manhattan Office</h3><p>415 Meridian Ave, Suite 1210<br>New York, NY 10099<br>(212) 555-0178</p></div>
  <div class="office"><h3>Long Island Office</h3><p>92 Orchard Mill Road<br>Great Neck, NY 11099<br>(516) 555-0163</p></div>
  <div class="office"><h3>Westchester Office</h3><p>260 Elm Street, 4th Floor<br>White Plains, NY 10699<br>(914) 555-0129</p></div>
  <div class="office"><h3>Staten Island Office</h3><p>Coming Soon<br>Coming Soon<br>Coming Soon</p></div>
  <div class="office"><h3>New Jersey Office</h3><p>Coming Soon<br>Coming Soon<br>Coming Soon</p></div>
</section>

<footer class="footer">
  <div class="links"><a href="#">Home</a> | <a href="#">Practice</a> | <a href="#">Areas</a> | <a href="#">Why Us</a> | <a href="#">Our Fees</a> | <a href="#">Free Advice</a> | <a href="#">Closing Tips</a> | <a href="#">Contact Us</a> | <a href="#">Languages</a></div>
  <p class="about">Our attorneys provide legal services throughout the five boroughs of New York City (Brooklyn, Manhattan, Queens, Staten Island, and the Bronx), Long Island (both Nassau &amp; Suffolk), Westchester County and Upstate New York. This website constitutes attorney advertising.</p>
  <p class="legal">© 2012 Thackeray Legal Group, All Rights Reserved &nbsp;&nbsp; Disclaimer | Privacy Policy | Site Map</p>
  <div class="social"><i></i><i></i><i></i><i></i><i></i></div>
</footer>
</body>
</html>
```